5x5 Pop Up Display, Company Logo With Text and Graphics for Tradeshow Display

Design for a 5ft x 5ft pop up trade show display that will sit on top of a table. I usually prefer clean, somewhat minimalist designs. We are a food service company but it's not a requirement to have photos of food. Design elements should compliment the table cloth that we have for the booth. The below may be included depending on the design aesthetic.
Service Provided: Daily Meal Service, Kitchen Management
"Nationwide Footprint"
"Grassroots Service"
"Fresh Scratch Cooking"
"Custom Menus"
"Made To Order Meals"

```html
<!DOCTYPE html>
<html lang="en">
<head>
<meta charset="utf-8">
<title>Hollis Hearth – Daily Meal Service Display</title>
<link rel="stylesheet" href="https://fonts.googleapis.com/css2?family=Domine:wght@400;700&family=Martel:wght@400&display=swap">
<style>
  :root {
    --ink: #141414;
    --accent-orange: #d6663c;
    --leaf-green: #7dc242;
    --deep-green: #4c8f2c;
    --rule-green: #d3e6b4;
    --paper: #ffffff;
    --page-bg: #e6e6e6;
  }
  html, body {
    margin: 0;
    padding: 0;
    width: 1200px;
    height: 1200px;
    overflow: hidden;
    background: var(--page-bg);
  }
  .display {
    position: relative;
    width: 1200px;
    height: 1200px;
    background: var(--paper);
    overflow: hidden;
  }
  .backdrop {
    position: absolute;
    inset: 0;
  }
  .brand {
    position: absolute;
    left: 44px;
    top: 70px;
    display: flex;
    align-items: center;
    gap: 18px;
  }
  .brand-name {
    font-family: "Domine", Georgia, serif;
    font-weight: 700;
    font-size: 74px;
    line-height: 0.95;
    color: var(--ink);
    text-transform: uppercase;
    letter-spacing: -1px;
  }
  .brand-dot {
    width: 40px;
    height: 40px;
    border-radius: 50%;
    background: var(--leaf-green);
    align-self: flex-start;
    margin-top: 6px;
  }
  .service-label {
    position: absolute;
    left: 46px;
    top: 250px;
    margin: 0;
    font-family: "Domine", Georgia, serif;
    font-weight: 700;
    font-size: 37px;
    color: var(--ink);
  }
  .service-title {
    position: absolute;
    left: 44px;
    top: 308px;
    margin: 0;
    font-family: "Domine", Georgia, serif;
    font-weight: 700;
    font-size: 90px;
    line-height: 0.92;
    color: var(--accent-orange);
    letter-spacing: -1px;
  }
  .service-secondary {
    position: absolute;
    left: 46px;
    top: 500px;
    margin: 0;
    font-family: "Domine", Georgia, serif;
    font-weight: 700;
    font-size: 40px;
    color: var(--ink);
  }
  .feature-list {
    position: absolute;
    left: 46px;
    top: 580px;
    width: 490px;
    margin: 0;
    padding: 0;
    list-style: none;
  }
  .feature-item {
    display: flex;
    align-items: center;
    gap: 26px;
    height: 79px;
    border-bottom: 2px solid var(--rule-green);
    font-family: "Martel", Georgia, serif;
    font-size: 31px;
    color: var(--ink);
  }
  .feature-item:last-child { border-bottom: none; }
  .feature-bullet {
    flex: none;
    width: 22px;
    height: 22px;
    border-radius: 50%;
    background: var(--leaf-green);
    box-shadow: inset 0 0 0 5px var(--accent-orange);
  }
</style>
</head>
<body>
<main class="display">
  <svg class="backdrop" width="1200" height="1200" viewBox="0 0 1200 1200" xmlns="http://www.w3.org/2000/svg">
    <defs>
      <linearGradient id="fruitTones" x1="0" y1="0" x2="0" y2="1">
        <stop offset="0" stop-color="#d9503a"/>
        <stop offset="0.3" stop-color="#e9c676"/>
        <stop offset="0.55" stop-color="#b8232b"/>
        <stop offset="1" stop-color="#4a1420"/>
      </linearGradient>
      <linearGradient id="hillTones" x1="0" y1="0" x2="0" y2="1">
        <stop offset="0" stop-color="#8fcf4e"/>
        <stop offset="1" stop-color="#5fa833"/>
      </linearGradient>
    </defs>

    <!-- green ring framing the hero photo -->
    <circle class="hero-ring" cx="1170" cy="640" r="640" fill="var(--leaf-green)"/>
    <circle class="hero-ring-inner" cx="1170" cy="640" r="624" fill="var(--paper)"/>
    <circle class="hero-photo" cx="1170" cy="640" r="612" fill="url(#fruitTones)"
            role="img" aria-label="Photograph of a platter of fresh cut fruit: strawberries, pineapple, grapes and melon"/>

    <!-- rolling green hills along the base -->
    <path class="base-hills" d="M0 1000 C 200 960, 420 990, 620 1060 C 820 1130, 1000 1090, 1200 1000 L1200 1200 L0 1200 Z"
          fill="url(#hillTones)"/>
    <path class="base-hills-shade" d="M0 1120 C 300 1090, 600 1130, 900 1150 C 1050 1160, 1130 1140, 1200 1120 L1200 1200 L0 1200 Z"
          fill="var(--deep-green)" opacity="0.55"/>

    <!-- illustration area: campus building with two servers -->
    <rect class="scene-illustration" x="110" y="975" width="440" height="225" rx="6" fill="#b9bcc0"
          role="img" aria-label="Illustration of a campus house with two staff members serving plated meals"/>

    <!-- illustration area: hand holding phone with ordering app -->
    <rect class="app-illustration" x="700" y="745" width="380" height="455" rx="30" fill="#6b9a4e"
          role="img" aria-label="Illustration of a hand holding a phone showing the mobile meal ordering app"/>
  </svg>

  <div class="brand">
    <div class="brand-name">Hollis<br>Hearth</div>
    <span class="brand-dot"></span>
  </div>

  <p class="service-label">Service Provided:</p>
  <h1 class="service-title">Daily Meal<br>Service</h1>
  <p class="service-secondary">Kitchen Management</p>

  <ul class="feature-list">
    <li class="feature-item"><span class="feature-bullet"></span>Nationwide Footprint</li>
    <li class="feature-item"><span class="feature-bullet"></span>Grassroots Service</li>
    <li class="feature-item"><span class="feature-bullet"></span>Fresh Scratch Cooking</li>
    <li class="feature-item"><span class="feature-bullet"></span>Custom Menus</li>
    <li class="feature-item"><span class="feature-bullet"></span>Made To Order Meals</li>
  </ul>
</main>
</body>
</html>
```